Historic Church website

We want our church website to feel warm, historic, and clean, modern, and easy to navigate. Dont use the anchor

Current website: https://www.meadowlarkfellowship.org/

Requirements
Should not have
• I would like to use the logo without the anchor

```html
<!DOCTYPE html>
<html lang="en">
<head>
<meta charset="utf-8">
<title>Meadowlark Fellowship Church</title>
<link rel="stylesheet" href="https://fonts.googleapis.com/css2?family=Cinzel:wght@400;600&family=Bebas+Neue&family=Poppins:wght@300;400;500;600&display=swap">
<style>
:root{
  --ink:#14100d;
  --dark:#1c1613;
  --brown:#3a2c22;
  --wood:#6a5343;
  --wood-dark:#4a3a2f;
  --tan:#c9ab83;
  --paper:#c9b59b;
  --cream:#f3ede6;
  --white:#ffffff;
  --line:#8a7a6c;
  --gold:#f2b01e;
  --muted:#cfc6bd;
}
*{box-sizing:border-box;margin:0;padding:0}
html,body{width:1200px;height:5080px;overflow:hidden}
body{background:var(--ink);color:var(--white);font-family:"Poppins",sans-serif;position:relative}
.abs{position:absolute}
section{position:absolute;left:0;width:1200px;overflow:hidden}
.serif{font-family:"Cinzel",serif}
.cond{font-family:"Bebas Neue",sans-serif}
.eyebrow{font-family:"Poppins",sans-serif;font-weight:600;font-size:15px;letter-spacing:3px;display:flex;align-items:center;gap:10px}
.eyebrow i{display:inline-block;width:44px;height:6px;border-top:1px solid currentColor;border-bottom:1px solid currentColor}
.center-label{justify-content:center;width:100%}
.btn{position:absolute;background:var(--tan);color:var(--ink);font-family:"Bebas Neue",sans-serif;font-size:18px;letter-spacing:.5px;display:flex;align-items:center;justify-content:center;gap:10px}
.btn .arr{width:18px;height:18px;border:1.5px solid var(--ink);border-radius:50%;display:flex;align-items:center;justify-content:center;font-family:"Poppins",sans-serif;font-size:10px}
.photo{position:absolute}
.brand{display:flex;flex-direction:column;align-items:center;gap:6px;font-family:"Cinzel",serif;font-weight:600;color:var(--white)}
.brand .dot{width:44px;height:44px;border:3px solid var(--white);border-radius:50%}
.brand .name{font-size:30px;letter-spacing:4px;line-height:1}
.brand .est{font-size:8px;letter-spacing:3px;font-family:"Poppins",sans-serif}

/* header / hero */
.hero{top:0;height:660px;background:linear-gradient(180deg,#3b2a20 0%,#5b3f2e 35%,#2b1e17 100%)}
.hero-photo{left:0;top:0;width:1200px;height:660px;background:radial-gradient(ellipse at 75% 35%,#a58466 0%,#6b4c38 35%,#2d1f17 75%)}
.topbar{top:12px;left:490px;display:flex;gap:30px;font-size:15px}
.topbar span{display:flex;align-items:center;gap:8px}
.topbar b{font-weight:600}
.ico{width:26px;height:26px;border-radius:50%;background:var(--white);display:inline-flex;align-items:center;justify-content:center}
.nav{top:76px;left:322px;display:flex;gap:30px;font-size:15px;color:var(--muted)}
.nav .on{color:var(--tan);font-weight:600}
.hero h1{position:absolute;left:100px;top:246px;font-family:"Cinzel",serif;font-weight:400;font-size:58px;line-height:66px;letter-spacing:1px}
.tagline{left:108px;top:410px;font-size:17px}

/* quote band */
.quote{top:640px;height:215px;background:var(--dark)}
.rule{position:absolute;left:113px;width:974px;height:1px;background:var(--line)}
.rule:before,.rule:after{content:"";position:absolute;top:-4px;width:9px;height:9px;border-radius:50%;background:var(--white)}
.rule:before{left:-4px}.rule:after{right:-4px}
.quote-text{position:absolute;width:100%;text-align:center;font-family:"Bebas Neue",sans-serif;font-size:40px;line-height:46px;letter-spacing:1px}

/* about */
.about{top:852px;height:625px;background:linear-gradient(180deg,#17120f,#1e1814)}
.about h2{position:absolute;left:612px;top:180px;font-family:"Cinzel",serif;font-weight:400;font-size:38px}
.about p{position:absolute;left:614px;top:245px;width:466px;font-size:15px;line-height:25px;color:var(--muted)}

/* flip */
.flip{top:1470px;height:695px;background:repeating-linear-gradient(90deg,#6e5646 0 140px,#655040 140px 142px,#725a49 142px 300px,#5f4a3c 300px 302px)}
.flip h2,.testi h2{position:absolute;width:100%;text-align:center;font-family:"Cinzel",serif;font-weight:400;font-size:39px}
.card{position:absolute;top:202px;width:310px;height:400px;background:var(--white);padding:8px;color:var(--ink);text-align:center}
.card .img{height:302px}
.card h3{font-family:"Bebas Neue",sans-serif;font-size:25px;font-weight:400;margin-top:16px}
.card .time{font-size:14px;margin-top:2px}
.card.active .img{height:384px;position:relative}
.card.active .over{position:absolute;left:0;bottom:0;width:100%;padding:0 20px 30px;color:var(--white);text-align:center;font-size:15px;line-height:23px}
.card.active .over h3{margin:0 0 4px}

/* independent */
.indep{top:2160px;height:590px;background:#120e0b}
.indep h2{position:absolute;left:105px;top:120px;font-family:"Cinzel",serif;font-weight:400;font-size:41px;line-height:46px}
.indep p{position:absolute;left:107px;top:316px;width:440px;font-size:15px;line-height:25px;color:var(--muted)}

/* sermon band */
.sermon{top:2745px;height:228px;background:linear-gradient(180deg,#2b221c,#3a2d24)}
.sermon .quote-text u{text-decoration-thickness:2px;text-underline-offset:6px}

/* testimonials */
.testi{top:2968px;height:630px;background:linear-gradient(180deg,#3a2b21,#2c2019)}
.tcard{position:absolute;top:182px;width:306px;height:328px;background:var(--cream);color:#333;text-align:center;padding-top:36px}
.tcard .mark{position:absolute;left:16px;top:-12px;width:32px;height:32px;border-radius:50%;background:var(--tan);color:var(--ink);font-family:"Cinzel",serif;font-size:24px;line-height:38px}
.tcard .avatar{width:64px;height:64px;border-radius:50%;margin:0 auto;background:linear-gradient(180deg,#b9b0a7,#776b61);border:3px solid var(--white)}
.stars{color:var(--gold);font-size:13px;letter-spacing:2px;margin-top:10px}
.tcard h4{font-size:19px;font-weight:600;color:var(--ink);margin-top:2px}
.tcard .role{font-size:15px;color:#777}
.tcard .say{font-size:15px;line-height:23px;color:#666;margin:14px 30px 0}
.side-arr{position:absolute;top:338px;font-size:34px;color:var(--muted);font-weight:300}
.dots{position:absolute;top:550px;left:0;width:100%;display:flex;justify-content:center;gap:20px}
.dots span{width:10px;height:10px;border-radius:50%;background:#6a5b50}
.dots .on{background:var(--white);box-shadow:0 0 0 3px #2c2019,0 0 0 4px var(--white)}

/* events */
.events{top:3590px;height:490px;background:linear-gradient(180deg,#1a1512,#231c17)}
.events h2{position:absolute;left:105px;top:186px;font-family:"Cinzel",serif;font-weight:400;font-size:41px;line-height:46px}
.circ{position:absolute;top:310px;width:40px;height:40px;border-radius:50%;display:flex;align-items:center;justify-content:center;font-size:18px;color:var(--ink)}
.ecard{position:absolute;top:100px;width:310px;height:300px;background:var(--white);color:var(--ink)}
.ecard .img{height:222px}
.ecard h3{font-family:"Bebas Neue",sans-serif;font-weight:400;font-size:25px;margin:14px 0 0 18px}
.ecard .more{font-family:"Bebas Neue",sans-serif;font-size:17px;margin-left:22px;display:flex;align-items:center;gap:8px}
.ecard .more span{width:16px;height:16px;border:1.5px solid var(--ink);border-radius:50%;font-family:"Poppins",sans-serif;font-size:9px;display:flex;align-items:center;justify-content:center}
.date{position:absolute;top:-14px;right:14px;width:60px;height:56px;background:var(--paper);border:3px solid var(--white);text-align:center;font-family:"Poppins",sans-serif;font-weight:600;font-size:13px;line-height:14px;padding-top:5px}

/* newsletter */
.news{top:4073px;height:390px;background:linear-gradient(180deg,#cbb79c,#bea98c);color:var(--ink)}
.news h2{position:absolute;width:100%;text-align:center;top:70px;font-family:"Cinzel",serif;font-weight:400;font-size:40px}
.field{position:absolute;left:380px;width:440px;height:52px;background:var(--white);border-radius:4px;display:flex;align-items:center;gap:8px;padding-left:18px;font-size:15px;color:#888}
.sub{position:absolute;left:485px;top:277px;width:230px;height:48px;background:#111;color:var(--white);font-family:"Bebas Neue",sans-serif;font-size:18px;display:flex;align-items:center;justify-content:center;gap:10px}
.sub span{width:17px;height:17px;border:1.5px solid var(--white);border-radius:50%;font-family:"Poppins",sans-serif;font-size:9px;display:flex;align-items:center;justify-content:center}

/* footer */
.footer{top:4455px;height:625px;background:#15110e}
.footer h5{position:absolute;top:130px;font-family:"Cinzel",serif;font-weight:400;font-size:17px;color:var(--tan);letter-spacing:1px}
.flinks{position:absolute;left:336px;top:188px;display:flex;flex-direction:column;gap:17px;font-size:15px;color:var(--muted)}
.contact{position:absolute;left:553px;font-size:15px;line-height:22px;color:var(--muted)}
.contact b{font-weight:500;color:var(--white)}
.cico{position:absolute;left:505px;width:32px;height:32px;border:1.5px solid var(--muted);border-radius:50%;display:flex;align-items:center;justify-content:center}
.thumb{position:absolute;width:84px;height:72px}
.social{position:absolute;top:332px;width:36px;height:36px;border-radius:50%;border:2px solid var(--white)}
.copy{position:absolute;top:555px;width:100%;text-align:center;font-size:13px;color:var(--muted)}
.copy em{font-style:normal;color:var(--tan)}
.torn{position:absolute;left:0;width:1200px}
</style>
</head>
<body>

<section class="hero">
  <div class="hero-photo" role="img" aria-label="Photograph of the historic sanctuary interior with timber ceiling and iron chandelier"></div>
  <div class="abs brand" style="left:120px;top:18px">
    <div class="dot"></div>
    <div class="name">MFC</div>
    <div class="est">EST. 1928</div>
  </div>
  <div class="abs topbar">
    <span><i class="ico"><svg width="13" height="13" viewBox="0 0 24 24"><path d="M3 6h18v12H3z M3 6l9 7 9-7" fill="none" stroke="#14100d" stroke-width="2"/></svg></i><b>Email :</b> info@MeadowlarkFellowship.org</span>
    <span><i class="ico"><svg width="13" height="13" viewBox="0 0 24 24"><path d="M6 3l4 4-2 3c1 3 3 5 6 6l3-2 4 4-3 3C10 21 3 14 3 6z" fill="#14100d"/></svg></i><b>Phone :</b> 310.555.0148</span>
  </div>
  <nav class="abs nav"><span class="on">Home</span><span>About MFC</span><span>Ministries</span><span>Bible Studies</span><span>Sermon Library</span></nav>
  <div class="btn" style="left:905px;top:64px;width:188px;height:50px">DONATE <span class="arr">→</span></div>
  <div class="abs eyebrow" style="left:105px;top:208px;letter-spacing:4px">FOUNDED IN 1928 <i></i></div>
  <h1>WELCOME TO<br>MEADOWLARK</h1>
  <div class="abs tagline">ANCIENT CHURCH. ANCIENT FAITH. ETERNAL TRUTH.</div>
  <div class="btn" style="left:105px;top:463px;width:258px;height:57px">JOIN OUR COMMUNITY <span class="arr">→</span></div>
</section>

<section class="quote">
  <svg class="torn" style="top:0" height="40" viewBox="0 0 1200 40" preserveAspectRatio="none"><path d="M0 0H1200V22L1160 14 1120 26 1070 12 1020 24 960 10 900 22 840 14 780 26 720 12 660 22 600 14 540 26 480 12 420 24 360 12 300 26 240 14 180 24 120 12 60 26 0 16Z" fill="#2b1e17"/></svg>
  <div class="rule" style="top:45px"></div>
  <div class="quote-text" style="top:66px">WE HAVE THIS HOPE AS AN ANCHOR FOR THE SOUL,<br>FIRM AND SECURE. - HEB 6:19</div>
  <div class="rule" style="top:180px"></div>
</section>

<section class="about">
  <svg class="abs" style="left:160px;top:70px" width="400" height="410" viewBox="0 0 400 410" role="img" aria-label="Photograph of the white church façade with arched wooden doors">
    <defs><linearGradient id="aboutPhoto" x1="0" y1="0" x2="1" y2="1"><stop offset="0" stop-color="#e9e3da"/><stop offset=".6" stop-color="#b8aa98"/><stop offset="1" stop-color="#5a4334"/></linearGradient></defs>
    <circle cx="200" cy="200" r="196" fill="#3c2f26"/>
    <circle cx="200" cy="200" r="170" fill="url(#aboutPhoto)"/>
    <rect x="10" y="370" width="380" height="30" fill="#3c2f26"/>
  </svg>
  <div class="abs eyebrow" style="left:608px;top:150px">WHO WE ARE <i></i></div>
  <h2>ABOUT MEADOWLARK</h2>
  <p>To all who worship with us, we offer a cordial welcome in the name of the Lord Jesus Christ. We endeavor to combine the warmth of gracious Christian hospitality with the fervor of a personal, devotional application of the great doctrines and eternal truths of God's Word. This church is committed to a Christ-honoring.</p>
  <div class="btn" style="left:614px;top:426px;width:188px;height:48px">READ MORE <span class="arr">→</span></div>
</section>

<section class="flip">
  <svg class="torn" style="top:0" height="36" viewBox="0 0 1200 36" preserveAspectRatio="none"><path d="M0 0H1200V18L1150 10 1100 24 1040 8 980 20 920 12 860 26 800 10 740 22 680 8 620 24 560 12 500 22 440 8 380 24 320 12 260 22 200 8 140 24 80 10 0 22Z" fill="#1e1814"/></svg>
  <div class="abs eyebrow center-label" style="top:84px;color:var(--white)"><i></i> VISIT US THIS SUNDAY <i></i></div>
  <h2 style="top:110px">FLIP THE BOXES FOR MORE INFORMATION</h2>
  <div class="card" style="left:105px">
    <div class="img" role="img" aria-label="Photograph of a wooden table beneath a framed map" style="background:linear-gradient(180deg,#a9917a,#5a4133 70%,#3a2a20)"></div>
    <h3>Morning Worship Service</h3>
    <div class="time">◷ 11:00 AM</div>
  </div>
  <div class="card active" style="left:445px">
    <div class="img" role="img" aria-label="Photograph of the church library with bookshelves" style="background:linear-gradient(180deg,#5b4a3e,#2a201a)">
      <div class="over" style="background:rgba(20,16,13,.55)">
        <h3>All Church Launch</h3>
        ◷ 12:15 PM<br>• Family Room •<br>Please join us for lunch<br>after the service.<br>Everyone is welcome!
      </div>
    </div>
  </div>
  <div class="card" style="left:785px">
    <div class="img" role="img" aria-label="Photograph of an antique wall clock above books" style="background:linear-gradient(180deg,#8e8578,#5d5348 60%,#b9a68b)"></div>
    <h3>Afternoon Adult Bible Study</h3>
    <div class="time">◷ 12:45 PM</div>
  </div>
</section>

<section class="indep">
  <div class="abs eyebrow" style="left:105px;top:92px">MEADOWLARK FELLOWSHIP CHURCH IS <i></i></div>
  <h2>AN INDEPENDENT<br>CHRISTIAN CHURCH IN<br>THE PROTESTANT<br>TRADITION</h2>
  <p>Its central tenets are found in its Articles of Faith and include belief in: the Deity and Lordship of Jesus Christ; the Trinity; Jesus' perfect life, atoning death on the cross, bodily resurrection,</p>
  <div class="btn" style="left:105px;top:446px;width:190px;height:50px">READ MORE <span class="arr">→</span></div>
  <svg class="abs" style="left:570px;top:100px" width="630" height="490" viewBox="0 0 630 490" role="img" aria-label="Photograph of the sanctuary with wooden pews and stained glass windows">
    <defs><linearGradient id="pews" x1="0" y1="0" x2="0" y2="1"><stop offset="0" stop-color="#5a3c2a"/><stop offset=".45" stop-color="#b59b83"/><stop offset=".7" stop-color="#4a2a20"/><stop offset="1" stop-color="#2a1812"/></linearGradient></defs>
    <path d="M170 0H630V490H0L60 300 110 220 140 120Z" fill="url(#pews)"/>
    <path d="M215 20H630" stroke="#8a7a6c" stroke-width="1.5"/>
  </svg>
</section>

<section class="sermon">
  <div class="rule" style="top:40px"></div>
  <div class="quote-text" style="top:60px">IF YOU CANNOT JOIN US IN PERSON<br><u>CLICK HERE</u> FOR THIS WEEK'S SERMON</div>
  <div class="rule" style="top:177px"></div>
</section>

<section class="testi">
  <div class="abs eyebrow center-label" style="top:56px"><i></i> TESTIMONIAL <i></i></div>
  <h2 style="top:80px">WHAT OUR CLIENT SAY ABOUT US</h2>
  <div class="side-arr" style="left:68px">‹</div>
  <div class="side-arr" style="left:1112px">›</div>
  <div class="tcard" style="left:107px"><div class="mark">“</div><div class="avatar" role="img" aria-label="Portrait photo"></div><div class="stars">★★★★★</div><h4>Elias R. Hartwell</h4><div class="role">MFC founder</div><div class="say">"The great need across evangelicalism is exposition of the ..(read more) "</div></div>
  <div class="tcard" style="left:447px"><div class="mark">“</div><div class="avatar" role="img" aria-label="Portrait photo"></div><div class="stars">★★★★★</div><h4>Thomas Ashby</h4><div class="role">Client</div><div class="say">"Christians are called to God's service not only in church. ..(read more) "</div></div>
  <div class="tcard" style="left:785px"><div class="mark">“</div><div class="avatar" role="img" aria-label="Portrait photo"></div><div class="stars">★★★★★</div><h4>Samuel Whitcombe</h4><div class="role">Client</div><div class="say">"To all who worship with us we extend a cordial welcome in the Name ..(read more) "</div></div>
  <div class="dots"><span class="on"></span><span></span><span></span><span></span></div>
</section>

<section class="events">
  <svg class="torn" style="top:0" height="30" viewBox="0 0 1200 30" preserveAspectRatio="none"><path d="M0 0H1200V14L1140 22 1080 8 1020 20 960 6 900 18 840 10 780 24 720 8 660 20 600 6 540 22 480 10 420 20 360 6 300 22 240 10 180 20 120 6 60 22 0 12Z" fill="#2c2019"/></svg>
  <div class="abs eyebrow" style="left:105px;top:140px">LATEST EVENT <i></i></div>
  <h2>UPCOMING<br>MFC EVENTS</h2>
  <div class="circ" style="left:105px;background:#8a8580">‹</div>
  <div class="circ" style="left:155px;background:var(--tan)">›</div>
  <div class="ecard" style="left:440px">
    <div class="img" role="img" aria-label="Photograph of a lit lantern at evening" style="background:radial-gradient(circle at 40% 40%,#f0c98a,#8a6a4a 40%,#2c221c 80%)"></div>
    <div class="date">WED<br>21<br>JAN</div>
    <h3>Wednesday Night Bible Study</h3>
    <div class="more">READ MORE <span>→</span></div>
  </div>
  <div class="ecard" style="left:783px">
    <div class="img" role="img" aria-label="Photograph of old bound books on a table" style="background:linear-gradient(180deg,#6f6a63,#4b4038 60%,#7a5a40)"></div>
    <div class="date">WED<br>25<br>JAN</div>
    <h3>Sunday Service</h3>
    <div class="more">READ MORE <span>→</span></div>
  </div>
</section>

<section class="news">
  <div class="abs" role="img" aria-label="Faint sketch of the church building" style="left:0;top:120px;width:320px;height:270px;background:linear-gradient(90deg,rgba(90,70,55,.28),rgba(90,70,55,0))"></div>
  <div class="abs eyebrow center-label" style="top:40px"><i></i> NEWSLETTER <i></i></div>
  <h2>SIGN UP FOR OUR WEEKLY NEWSLETTER</h2>
  <div class="field" style="top:140px">👤︎ Enter Your Name</div>
  <div class="field" style="top:206px">✉︎ Enter Your Email</div>
  <div class="sub">SUBSCRIBE NOW <span>→</span></div>
  <svg class="torn" style="bottom:0" height="30" viewBox="0 0 1200 30" preserveAspectRatio="none"><path d="M0 30H1200V14L1150 4 1090 18 1030 6 970 20 910 8 850 22 790 6 730 18 670 8 610 22 550 6 490 20 430 8 370 18 310 4 250 20 190 8 130 22 70 6 0 18Z" fill="#15110e"/></svg>
</section>

<section class="footer">
  <div class="abs brand" style="left:120px;top:130px">
    <div class="dot"></div>
    <div class="name">MFC</div>
    <div class="est">EST. 1928</div>
  </div>
  <div class="social" style="left:105px" aria-label="Social link"></div>
  <div class="social" style="left:152px" aria-label="Social link"></div>
  <div class="social" style="left:198px" aria-label="Social link"></div>
  <div class="social" style="left:244px" aria-label="Social link"></div>

  <h5 style="left:336px">QUICK LINK</h5>
  <div class="flinks"><span>Home</span><span>About MFC</span><span>Ministries</span><span>Bible Studies</span><span>Sermon Library</span></div>

  <h5 style="left:503px">QUICK CONTACT</h5>
  <div class="cico" style="top:190px"><svg width="14" height="14" viewBox="0 0 24 24"><path d="M12 2a7 7 0 0 0-7 7c0 5 7 13 7 13s7-8 7-13a7 7 0 0 0-7-7zm0 9.5A2.5 2.5 0 1 1 12 6.5a2.5 2.5 0 0 1 0 5z" fill="#cfc6bd"/></svg></div>
  <div class="contact" style="top:188px"><b>Location :</b><br>2240 Linden Avenue<br>Los Angeles, California<br>90011</div>
  <div class="cico" style="top:318px"><svg width="14" height="14" viewBox="0 0 24 24"><path d="M6 3l4 4-2 3c1 3 3 5 6 6l3-2 4 4-3 3C10 21 3 14 3 6z" fill="#cfc6bd"/></svg></div>
  <div class="contact" style="top:316px"><b>Phone :</b><br>310.555.0148</div>
  <div class="cico" style="top:392px"><svg width="14" height="14" viewBox="0 0 24 24"><path d="M3 6h18v12H3z M3 6l9 7 9-7" fill="none" stroke="#cfc6bd" stroke-width="2"/></svg></div>
  <div class="contact" style="top:390px"><b>Email :</b><br>info@MeadowlarkFellowship.org</div>

  <h5 style="left:820px">MFC SERMONS</h5>
  <div class="thumb" role="img" aria-label="Sermon artwork" style="left:822px;top:175px;background:linear-gradient(135deg,#8a7a6a,#3b302a)"></div>
  <div class="thumb" role="img" aria-label="Sermon artwork" style="left:913px;top:175px;background:linear-gradient(135deg,#a88d60,#3e3020)"></div>
  <div class="thumb" role="img" aria-label="Sermon artwork" style="left:1008px;top:175px;background:linear-gradient(135deg,#c0622a,#3a1a10)"></div>
  <div class="thumb" role="img" aria-label="Sermon artwork" style="left:822px;top:260px;background:linear-gradient(135deg,#7a6e60,#2a2420)"></div>
  <div class="thumb" role="img" aria-label="Sermon artwork" style="left:913px;top:260px;background:linear-gradient(135deg,#2a5a6a,#a06a2a)"></div>
  <div class="thumb" role="img" aria-label="Sermon artwork" style="left:1008px;top:260px;background:linear-gradient(135deg,#6a4a2a,#2a1a10)"></div>
  <div class="thumb" role="img" aria-label="Sermon artwork" style="left:822px;top:345px;background:linear-gradient(135deg,#6a8aa0,#3a4a30)"></div>
  <div class="thumb" role="img" aria-label="Sermon artwork" style="left:913px;top:345px;background:linear-gradient(135deg,#1a2a40,#c09030)"></div>
  <div class="thumb" role="img" aria-label="Sermon artwork" style="left:1008px;top:345px;background:linear-gradient(135deg,#b0a898,#4a4238)"></div>

  <div class="abs" style="left:0;top:520px;width:1200px;height:1px;background:#2e2621"></div>
  <div class="copy">© Copyright 2026 &nbsp;| &nbsp;<em>Meadowlark Fellowship Church, Westbrook</em>, Los Angeles, California, &nbsp;All Rights Reserved</div>
</section>

</body>
</html>
```